Chicago Property Management Flyer

We need a brochure/flyer to market our property management services to Chicago property owners. I believe that my preference is single page, double sided, but a bi-fold or tri-fold format may also work. I have provided our logo, and some example images in case that is helpful. Refer to our website at http://www.velmorehq.net/ for more info.

Industry/Entity Type

Property Management

Font styles to use
Sans Serif

```html
<!DOCTYPE html>
<html lang="en">
<head>
<meta charset="utf-8">
<title>Velmore Property Management Flyer</title>
<link rel="stylesheet" href="https://fonts.googleapis.com/css2?family=Catamaran:wght@300;400;500;700;800&display=swap">
<style>
:root{
  --blue:#1d6fb8;
  --navy:#1c4f7d;
  --ink:#1f1f1f;
  --body:#3a3a3a;
  --paper:#ffffff;
  --mist:#eeeeee;
  --footer:#15528a;
}
*{box-sizing:border-box;margin:0;padding:0}
html,body{width:1200px;height:864px;overflow:hidden;background:var(--paper)}
body{position:relative;font-family:"Catamaran",Arial,sans-serif;color:var(--ink)}
.page{position:absolute;top:25px;width:575px;height:813px;overflow:hidden;
  background:linear-gradient(180deg,var(--mist) 0%,#fff 16%,#fff 100%)}
.page--front{left:18px}
.page--back{left:610px}
.top-swoosh{position:absolute;left:0;top:0;width:575px;height:60px}

/* front */
.brand{position:absolute;left:42px;top:70px;width:230px;text-align:center;font-weight:800;color:var(--navy);line-height:1}
.brand__mark{display:block;width:34px;height:34px;margin:0 auto 10px;background:var(--navy)}
.brand__name{display:block;font-size:21px;letter-spacing:.3px}
.brand__sub{display:block;font-size:13px;letter-spacing:3px;margin-top:3px;color:#3b3b3b}
.site-url{position:absolute;right:38px;top:78px;font-size:13px;font-weight:500;color:var(--ink)}
.headline{position:absolute;left:46px;top:190px;width:390px;font-size:36px;font-weight:400;line-height:39px;color:var(--ink)}
.subhead{position:absolute;left:48px;top:323px;width:360px;font-size:20px;font-weight:400;line-height:25px;color:var(--blue)}
.city-photo{position:absolute;left:0;bottom:0;width:575px;height:358px;
  background:linear-gradient(180deg,#bdbdbd 0%,#8e8e8e 22%,#5e5e5e 50%,#3a3a3a 80%,#262626 100%)}
.front-watermark{position:absolute;left:50px;bottom:24px;font-size:26px;font-weight:800;letter-spacing:.5px;color:rgba(255,255,255,.28)}
.wave{position:absolute;left:0;width:575px}

/* back */
.section-title{position:absolute;left:48px;top:44px;font-size:19px;font-weight:500;color:var(--ink)}
.intro{position:absolute;left:49px;top:70px;width:495px;font-size:13.5px;font-weight:300;line-height:16.5px;color:var(--blue)}
.intro p+p{margin-top:4px}
.feature{position:absolute;width:172px}
.feature--right{width:190px}
.feature__icon{position:absolute;left:-60px;top:0;width:44px;height:44px}
.feature__title{font-size:12px;font-weight:500;color:var(--ink);line-height:15px}
.feature__text{font-size:11.6px;font-weight:400;color:var(--body);line-height:14.9px}
.skyline-photo{position:absolute;left:0;bottom:0;width:575px;height:235px;
  background:linear-gradient(180deg,#e6e6e6 0%,#a9a9a9 35%,#6a6a6a 70%,#4a4a4a 100%)}
.contact-band{position:absolute;left:0;bottom:20px;width:575px;height:44px;background:rgba(21,82,138,.92);color:#fff}
.contact-band__org{position:absolute;left:49px;top:6px;font-size:13.5px;line-height:16px}
.contact-band__org strong{font-weight:700}
.contact-band__reach{position:absolute;left:358px;top:2px;font-size:15px;line-height:21px}
.contact-band__reach svg{vertical-align:-2px;margin-right:10px}
</style>
</head>
<body>

<section class="page page--front">
  <svg class="top-swoosh" viewBox="0 0 575 60" aria-hidden="true">
    <path d="M150 0 C300 10 450 40 575 30 L575 0 Z" fill="#e4e4e4"/>
    <path d="M200 0 C330 14 460 30 575 20" fill="none" stroke="#d6d6d6" stroke-width="2"/>
  </svg>

  <div class="brand">
    <span class="brand__mark"></span>
    <span class="brand__name">VELMORE PROPERTY</span>
    <span class="brand__sub">MANAGEMENT</span>
  </div>
  <div class="site-url">www.velmorehq.net</div>

  <h1 class="headline">Managing Apartment Buildings across Chicago for over a Decade.</h1>
  <p class="subhead">Leverage our experience and expertise to succeed with your properties.</p>

  <div class="city-photo" role="img" aria-label="Black and white aerial photo of the Chicago skyline along the lakefront"></div>
  <svg class="wave" style="top:375px;height:110px" viewBox="0 0 575 110" aria-hidden="true">
    <defs>
      <linearGradient id="fw" x1="0" x2="1"><stop offset="0" stop-color="#1d6fb8"/><stop offset=".5" stop-color="#6db4e8"/><stop offset="1" stop-color="#1d6fb8"/></linearGradient>
    </defs>
    <path d="M0 30 C120 60 220 80 330 66 C430 52 500 26 575 20 L575 50 C480 60 420 90 320 94 C200 98 110 66 0 54 Z" fill="url(#fw)" opacity=".9"/>
    <path d="M0 50 C140 74 250 100 360 88 C450 78 520 54 575 48 L575 66 C500 76 430 104 340 106 C220 108 120 84 0 70 Z" fill="#3e93d6" opacity=".55"/>
    <path d="M0 62 C160 96 300 66 420 56 C500 50 540 54 575 60" fill="none" stroke="#9bcdf0" stroke-width="4" opacity=".8"/>
  </svg>
  <div class="front-watermark">VELMORE PROPERTY MANAGEMENT</div>
</section>

<section class="page page--back">
  <svg class="top-swoosh" viewBox="0 0 575 60" aria-hidden="true">
    <path d="M150 0 C300 10 450 40 575 30 L575 0 Z" fill="#e4e4e4"/>
  </svg>

  <h2 class="section-title">Who We Are</h2>
  <div class="intro">
    <p>We have been managing apartment buildings across Chicago for over a decade.<br>We believe strong business systems and processes are what make property management successful for property owners.</p>
    <p>Our use of technology helps us to track and share information with our property owners, tenants, and management team. Our established systems allow us to quickly and cost-effectively manage your property’s maintenance issues, tenant issues, and leasing needs.</p>
  </div>

  <div class="feature" style="left:93px;top:215px">
    <svg class="feature__icon" viewBox="0 0 44 44" aria-hidden="true"><circle cx="24" cy="22" r="15" fill="none" stroke="var(--blue)" stroke-width="3"/><path d="M24 12v10l7 5" fill="none" stroke="var(--blue)" stroke-width="3" stroke-linecap="round"/><path d="M4 20l5 6 5-6" fill="var(--blue)"/></svg>
    <div class="feature__title">Save Time and Headaches</div>
    <div class="feature__text">We have a team in place to tackle all aspects of property management for you. Never worry about leasing, tenants, maintenance, regulations, etc.</div>
  </div>
  <div class="feature" style="left:93px;top:319px">
    <svg class="feature__icon" viewBox="0 0 44 44" aria-hidden="true"><g fill="var(--blue)"><ellipse cx="14" cy="30" rx="12" ry="5"/><ellipse cx="14" cy="24" rx="12" ry="5"/><ellipse cx="32" cy="26" rx="11" ry="5"/><ellipse cx="32" cy="20" rx="11" ry="5"/><ellipse cx="32" cy="14" rx="11" ry="5"/></g></svg>
    <div class="feature__title">Maximize Your Investment Assets</div>
    <div class="feature__text">Your properties are expensive assets with lots of potential. Put the right professionals in place to protect, maintain, and maximize their value.</div>
  </div>
  <div class="feature" style="left:93px;top:423px">
    <svg class="feature__icon" viewBox="0 0 44 44" aria-hidden="true"><g fill="var(--blue)"><rect x="4" y="28" width="5" height="12"/><rect x="11" y="22" width="5" height="18"/><rect x="18" y="14" width="5" height="26"/><path d="M14 10l6-8 6 8z"/><circle cx="32" cy="30" r="9"/></g><text x="32" y="35" font-size="13" fill="#fff" text-anchor="middle" font-family="Arial,sans-serif" font-weight="700">$</text></svg>
    <div class="feature__title">Increase Income</div>
    <div class="feature__text">With our experience and market knowledge we can establish optimal rent prices, lease apartments quickly, reduce turnover, and navigate complex housing agency processes to ensure maximum income to you.</div>
  </div>

  <div class="feature feature--right" style="left:350px;top:215px">
    <svg class="feature__icon" style="left:-50px" viewBox="0 0 44 44" aria-hidden="true"><path d="M12 2h12v18h8L18 40 4 20h8z" fill="var(--blue)"/><text x="18" y="26" font-size="14" fill="#fff" text-anchor="middle" font-family="Arial,sans-serif" font-weight="700">$</text></svg>
    <div class="feature__title">Reduce Expenses, Maximize Profits</div>
    <div class="feature__text">Maximize your profits by benefitting from our economies of scale, systems and processes, specialized knowledge, industry network, and buying power</div>
  </div>
  <div class="feature feature--right" style="left:350px;top:319px">
    <svg class="feature__icon" style="left:-50px" viewBox="0 0 44 44" aria-hidden="true"><rect x="4" y="2" width="22" height="40" rx="3" fill="none" stroke="var(--blue)" stroke-width="3"/><circle cx="24" cy="20" r="11" fill="var(--blue)"/><text x="24" y="25" font-size="13" fill="#fff" text-anchor="middle" font-family="Arial,sans-serif" font-weight="700">i</text></svg>
    <div class="feature__title">Stay Informed</div>
    <div class="feature__text">With access to all of your property information, documentation, and financials through your online portal of our property management system you and your accountant can stay informed as needed</div>
  </div>
  <div class="feature feature--right" style="left:350px;top:453px">
    <svg class="feature__icon" style="left:-58px" viewBox="0 0 44 44" aria-hidden="true"><g fill="var(--blue)"><rect x="4" y="30" width="6" height="10"/><rect x="13" y="26" width="6" height="14"/><rect x="22" y="30" width="6" height="10"/><rect x="31" y="22" width="6" height="18"/></g><path d="M3 26l10-10 9 8 14-14" fill="none" stroke="var(--blue)" stroke-width="4"/><path d="M32 6h9v9z" fill="var(--blue)"/></svg>
    <div class="feature__title">Grow Your Investment Portfolio</div>
    <div class="feature__text">With our management team focused on profitably managing your existing properties, we can then help you expand to future investments</div>
  </div>

  <div class="skyline-photo" role="img" aria-label="Black and white photo of the downtown Chicago skyline"></div>
  <svg class="wave" style="top:552px;height:100px" viewBox="0 0 575 100" aria-hidden="true">
    <defs>
      <linearGradient id="bw" x1="0" x2="1"><stop offset="0" stop-color="#1d6fb8"/><stop offset=".5" stop-color="#7fc0ec"/><stop offset="1" stop-color="#1d6fb8"/></linearGradient>
    </defs>
    <path d="M0 16 C120 40 220 60 330 48 C430 36 500 20 575 16 L575 42 C480 50 420 74 320 78 C200 82 110 50 0 38 Z" fill="url(#bw)" opacity=".9"/>
    <path d="M0 36 C140 60 250 86 360 74 C450 64 520 42 575 38 L575 70 C500 74 430 94 340 96 C220 98 120 72 0 56 Z" fill="#3e93d6" opacity=".5"/>
  </svg>

  <div class="contact-band">
    <div class="contact-band__org"><strong>Velmore Property Management</strong><br>1180 W. Harlow St, Chicago IL 60608</div>
    <div class="contact-band__reach">
      <div><svg width="14" height="14" viewBox="0 0 14 14" aria-hidden="true"><path d="M3 1l3 3-2 2c1 2 2 3 4 4l2-2 3 3-2 2C6 13 1 8 1 3z" fill="#fff"/></svg>773-555-0148</div>
      <div><svg width="14" height="11" viewBox="0 0 14 11" aria-hidden="true"><rect x="0.5" y="0.5" width="13" height="10" fill="none" stroke="#fff"/><path d="M1 1l6 5 6-5" fill="none" stroke="#fff"/></svg>dana@velmorehq.net</div>
    </div>
  </div>
</section>

</body>
</html>
```